Book Cover Design Project

Cover design using photo provided.
Title is as follows:-

Harold Edmund Tessler

"Marching beside the Quiet Harbour"

By Dennis Palgrave

Just Added Picture and extended design a further 7 days

```html
<!DOCTYPE html>
<html lang="en">
<head>
<meta charset="utf-8">
<title>Marching beside the Quiet Harbour – Book Cover</title>
<link rel="stylesheet" href="https://fonts.googleapis.com/css2?family=Cabin:wght@500;600&family=Oswald:wght@400;500&display=swap">
<style>
  :root {
    --stage: #c9c9c9;
    --sky-top: #4a8fd6;
    --sky-mid: #8fb8d9;
    --haze: #9c8a6a;
    --earth: #8a4f1c;
    --earth-deep: #3e220e;
    --portrait-light: #d8cfa0;
    --portrait-mid: #6b5a3c;
    --portrait-dark: #1f1c1c;
    --gold: #d9a52e;
    --gold-soft: #c99530;
  }
  * { margin: 0; padding: 0; box-sizing: border-box; }
  html, body {
    width: 1200px;
    height: 861px;
    overflow: hidden;
    background: var(--stage);
  }
  .canvas {
    position: relative;
    width: 1200px;
    height: 861px;
  }
  .cover {
    position: absolute;
    left: 380px;
    top: 91px;
    width: 440px;
    height: 680px;
    overflow: hidden;
  }
  .cover-art {
    position: absolute;
    inset: 0;
    background:
      linear-gradient(180deg,
        var(--sky-top) 0%,
        var(--sky-mid) 38%,
        var(--haze) 58%,
        var(--earth) 78%,
        var(--earth-deep) 100%);
  }
  .portrait {
    position: absolute;
    left: 50px;
    top: 24px;
    width: 360px;
    height: 420px;
    border-radius: 46% 46% 8% 8% / 34% 34% 6% 6%;
    background:
      radial-gradient(ellipse 32% 28% at 48% 40%, var(--portrait-light) 0%, var(--portrait-mid) 70%, transparent 100%),
      linear-gradient(180deg, var(--portrait-dark) 0%, var(--portrait-mid) 22%, var(--portrait-dark) 60%, rgba(31,28,28,0) 100%);
    opacity: 0.92;
  }
  .cover-text {
    position: absolute;
    left: 0;
    right: 0;
    text-align: center;
    color: var(--gold);
  }
  .subject-name {
    top: 408px;
    font-family: "Cabin", sans-serif;
    font-weight: 600;
    font-size: 20px;
    letter-spacing: 0.5px;
  }
  .title-lead {
    top: 448px;
    font-family: "Oswald", sans-serif;
    font-weight: 400;
    font-size: 24px;
    letter-spacing: 9px;
    color: var(--gold-soft);
  }
  .title-main {
    top: 478px;
    font-family: "Oswald", sans-serif;
    font-weight: 500;
    font-size: 62px;
    line-height: 1;
    letter-spacing: 1px;
  }
  .author {
    top: 568px;
    font-family: "Cabin", sans-serif;
    font-weight: 500;
    font-size: 21px;
    letter-spacing: 0.5px;
  }
</style>
</head>
<body>
<main class="canvas">
  <section class="cover">
    <div class="cover-art" role="img" aria-label="Blue sky with clouds and vapour trails above fighter planes flying low over a warm brown textured landscape"></div>
    <div class="portrait" role="img" aria-label="Head and shoulders portrait of an airman in dark uniform, shirt, tie and side cap"></div>
    <p class="cover-text subject-name">HAROLD EDMUND TESSLER</p>
    <p class="cover-text title-lead">MARCHING BESIDE THE</p>
    <h1 class="cover-text title-main">QUIET HARBOUR</h1>
    <p class="cover-text author">BY DENNIS PALGRAVE</p>
  </section>
</main>
</body>
</html>
```